Marlow Law Stationery - Letterhead, Envelopes, Business Cards

We need high quality business stationery for our Personal Injury Law Firm located in Houston, Texas. The design should include the logo, Marlow Law Group, PLLC, 713-555-4718, 2150 Fernbrook Avenue, Suite 310, Houston, Texas 77019 www.MarlowLaw.example. The colors are blue and white. The letterhead should also include the Attorneys - Tessa Quill, Mitchell R. Marlow and Derek Hale.

```html
<!DOCTYPE html>
<html lang="en">
<head>
<meta charset="utf-8">
<title>Marlow Law Stationery</title>
<link href="https://fonts.googleapis.com/css2?family=Montserrat:wght@400;600;700&family=Cormorant+SC:wght@500&family=Arimo:wght@400&display=swap" rel="stylesheet">
<style>
:root{
  --navy:#2c3d68;
  --navy-deep:#1f2c4f;
  --navy-soft:#3a4c76;
  --paper:#ffffff;
  --ground:#e8e9eb;
  --ink:#3a3d44;
  --rule:#c9ccd2;
  --muted:#6b6f78;
}
*{margin:0;padding:0;box-sizing:border-box}
html,body{width:1200px;height:800px;overflow:hidden;background:var(--ground)}
body{position:relative;font-family:"Montserrat",sans-serif;color:var(--ink)}
.piece{position:absolute;background:var(--paper);box-shadow:0 1px 3px rgba(0,0,0,.12)}
.mark{display:flex;align-items:center;gap:4px;font-family:"Montserrat",sans-serif;font-weight:700;white-space:nowrap}
.mark .dot{border-radius:50%;flex:none}
.mark--navy{color:var(--navy)}
.mark--navy .dot{background:var(--navy)}
.mark--white{color:var(--paper)}
.mark--white .dot{background:var(--paper)}

/* banner */
.banner{left:183px;top:33px;width:847px;height:84px;background:linear-gradient(180deg,var(--navy-soft),var(--navy-deep));border-radius:10px;display:flex;align-items:center;justify-content:center}
.banner .mark{font-size:18px}.banner .dot{width:14px;height:14px}

/* notepad */
.notepad{left:216px;top:156px;width:141px;height:193px;padding:10px 12px}
.notepad .mark{font-size:6px;justify-content:center;margin-bottom:8px}
.notepad .dot{width:6px;height:6px}
.notepad .lines{height:148px;background:repeating-linear-gradient(180deg,transparent 0 7.5px,var(--rule) 7.5px 8.2px)}

/* letterhead */
.letterhead{left:398px;top:146px;width:280px;height:396px;padding:26px 33px 0}
.lh-head{display:flex;justify-content:space-between}
.lh-brand .group{font-size:4.6px;font-weight:700;color:var(--navy)}
.lh-brand .title{font-size:9px;font-weight:700;color:var(--navy);line-height:1.05;text-align:center}
.lh-brand .mark{font-size:6px;margin-bottom:2px}.lh-brand .dot{width:6px;height:6px}
.attorneys{font-family:"Cormorant SC",serif;font-size:6.3px;color:var(--muted);line-height:1.1}
.lh-body{font-family:"Arimo",sans-serif;font-size:4.3px;line-height:1.42;color:var(--ink)}
.address{margin-top:46px}
.salute{margin-top:30px;margin-bottom:6px}
.lh-body p{margin-bottom:5px;text-align:justify}
.signature{width:62px;height:22px;margin:6px 0 6px;background:linear-gradient(90deg,rgba(44,61,104,.12),rgba(44,61,104,.02))}
.lh-foot{position:absolute;left:33px;right:33px;bottom:16px;border-top:.6px solid var(--muted);padding-top:5px;text-align:center;font-size:5.8px;color:var(--muted);line-height:1.4}
.lh-foot svg{width:5px;height:5px;vertical-align:-0.5px;fill:var(--navy)}

/* folder */
.folder{left:697px;top:148px;width:305px;height:417px;background:linear-gradient(180deg,var(--navy-soft),var(--navy))}
.folder::after{content:"";position:absolute;top:0;bottom:0;left:263px;width:1px;background:rgba(255,255,255,.85)}
.folder-face{position:absolute;left:0;top:0;width:263px;height:100%;display:flex;flex-direction:column;align-items:center}
.folder .mark{font-size:22px;margin-top:190px;gap:8px}
.folder .dot{width:20px;height:20px}
.folder .url{margin-top:auto;margin-bottom:30px;font-size:10px;color:var(--paper)}

/* business cards */
.card{left:246px;width:111px;height:67px}
.card-front{top:386px;padding:13px 10px 0}
.card-front .brand{display:flex;justify-content:flex-end}
.card-front .brand .mark{font-size:5.5px}.card-front .dot{width:6px;height:6px}
.card-front .name{margin-top:6px;font-size:3.6px;font-weight:700;color:var(--navy)}
.card-front .role{font-size:2.6px;color:var(--muted);border-bottom:.4px solid var(--muted);padding-bottom:2px}
.card-front .info{display:flex;justify-content:space-between;font-size:2.5px;color:var(--muted);margin-top:4px;line-height:1.35}
.card-front .info .right{text-align:right}
.card-back{top:476px;background:linear-gradient(180deg,var(--navy-soft),var(--navy-deep));display:flex;align-items:center;justify-content:center}
.card-back .mark{font-size:10px}.card-back .dot{width:9px;height:9px}

/* envelopes */
.env-front{left:288px;top:610px;width:292px;height:146px;padding:20px 14px}
.env-front .group{font-size:4.2px;font-weight:700;color:var(--navy)}
.env-front .title{font-size:8px;font-weight:700;color:var(--navy);line-height:1.05}
.env-front .mark{font-size:6px;margin-bottom:2px}.env-front .dot{width:8px;height:8px}
.env-front .addr{font-size:5.4px;color:var(--muted);line-height:1.15;text-align:center;width:74px;margin-top:8px}
.env-back{left:383px;top:567px;width:293px;height:147px}
.env-back .flap{height:41px;background:linear-gradient(180deg,var(--navy-soft),var(--navy));border-radius:0 0 6px 6px;display:flex;align-items:center;justify-content:center}
.env-back .mark{font-size:8px}.env-back .dot{width:7px;height:7px}

/* stickers */
.sticker{position:absolute;top:725px;width:33px;height:33px;border-radius:50%;background:var(--navy);display:flex;align-items:center;justify-content:center;box-shadow:0 1px 3px rgba(0,0,0,.2)}
.sticker .mark{font-size:4.6px;gap:2px}.sticker .dot{width:3px;height:3px}
</style>
</head>
<body>

<div class="piece banner"><div class="mark mark--white"><span class="dot"></span>Marlow Law</div></div>

<div class="piece notepad">
  <div class="mark mark--navy"><span class="dot"></span>Marlow Law</div>
  <div class="lines"></div>
</div>

<div class="piece letterhead">
  <div class="lh-head">
    <div class="lh-brand">
      <div class="mark mark--navy"><span class="dot"></span>Marlow Law</div>
      <div class="group">MARLOW LAW GROUP, PLLC</div>
      <div class="title">INJURY<br>ATTORNEYS</div>
    </div>
    <div class="attorneys">Attorneys<br>Tessa Quill,<br>Mitchell R. Marlow<br>and Derek Hale</div>
  </div>
  <div class="lh-body">
    <div class="address">First Name Last Name<br>Addressee's name<br>Building number/name and street<br>Post Town, Post Code</div>
    <div class="salute">Dear First Name</div>
    <p>Lorem ipsum dolor sit amet, consectetur adipiscing elit. Vestibulum eu vulputate sapien. In quis imperdiet lectus, eget accumsan sem. Vestibulum consequat rhoncus cursus. Quisque ultrices facilisis libero, eu facilisis nisl congue sit amet. Phasellus consequat justo mi. In sollicitudin justo sed eros blandit, non eleifend elit faucibus. Aliquam elit purus, facilisis at pulvinar eu, rutrum ut mauris. Suspendisse aliquam ipsum vitae egestas venenatis. Quisque a lacinia orci, sit amet tincidunt diam. Nulla blandit justo sit amet purus gravida, pulvinar iaculis sapien egestas. Sed vehicula diam leo, et vehicula leo elementum et. Duis nec suscipit justo. Maecenas eget pretium leo. Quisque imperdiet ut quam ut placerat. Duis facilisis, nisi sit amet dictum egestas, neque nulla elementum nibh, in ultrices mi magna nec metus.</p>
    <p>Duis arcu lacus, accumsan id lectus eu, condimentum tincidunt purus. Cras ac justo sed odio mattis gravida consectetur ac sapien. Integer eleifend enim et ipsum fermentum auctor. Quisque at porttitor velit. Aenean gravida nibh odio, eget tempus mauris semper at. In consectetur sed leo ut molestie. Sed pharetra urna quis turpis fringilla, ut posuere massa hendrerit. Proin pulvinar nibh augue, vel luctus elit aliquet non. Nunc elementum iaculis turpis eu interdum. Pellentesque non imperdiet magna, ut facilisis augue.</p>
    <div>Sincerely,</div>
    <div class="signature" role="img" aria-label="Handwritten signature"></div>
    <div>First Name Last Name<br>Position</div>
  </div>
  <div class="lh-foot">
    2150 Fernbrook Avenue, Suite 310, Houston, Texas 77019<br>
    <svg viewBox="0 0 10 10"><path d="M0 2h10v6H0z"/></svg> info@marlowlaw.example &nbsp;
    <svg viewBox="0 0 10 10"><path d="M2 1l2 2-1 1.5c.6 1.3 1.4 2.1 2.5 2.5L7 6l2 2-1.5 1.5C4 9 1 6 .5 2.5z"/></svg> 713-555-4718 &nbsp;
    <svg viewBox="0 0 10 10"><circle cx="5" cy="5" r="5"/></svg> www.marlowlaw.example
  </div>
</div>

<div class="piece folder">
  <div class="folder-face">
    <div class="mark mark--white"><span class="dot"></span>Marlow Law</div>
    <div class="url">www.marlowlaw.example</div>
  </div>
</div>

<div class="piece card card-front">
  <div class="brand"><div class="mark mark--navy"><span class="dot"></span>Marlow Law</div></div>
  <div class="name">TESSA QUILL</div>
  <div class="role">Attorney Of Law</div>
  <div class="info">
    <div>713-555-4718<br>info@marlowlaw.example<br>www.marlowlaw.example</div>
    <div class="right">2150 Fernbrook Avenue<br>Suite 310 Houston,<br>Texas 77019</div>
  </div>
</div>
<div class="piece card card-back"><div class="mark mark--white"><span class="dot"></span>Marlow Law</div></div>

<div class="piece env-front">
  <div class="mark mark--navy"><span class="dot"></span>Marlow Law</div>
  <div class="group">MARLOW LAW GROUP, PLLC</div>
  <div class="title">INJURY<br>ATTORNEYS</div>
  <div class="addr">2150 Fernbrook Avenue<br>Suite 310 Houston,<br>Texas 77019</div>
</div>
<div class="piece env-back">
  <div class="flap"><div class="mark mark--white"><span class="dot"></span>Marlow Law</div></div>
</div>

<div class="sticker" style="left:596px"><div class="mark mark--white"><span class="dot"></span>Marlow</div></div>
<div class="sticker" style="left:648px"><div class="mark mark--white"><span class="dot"></span>Marlow</div></div>
<div class="sticker" style="left:701px"><div class="mark mark--white"><span class="dot"></span>Marlow</div></div>

</body>
</html>
```